Flyer-Design für Keramik Verdunster
Zielgruppe
Wir wollen Keramik Verdunster bei Volkarn Verkaufen und dieser Flyer soll in jede Produktverpackung mit hinein gelegt werden.
Aufgabenstellung
Der Flyer sollte möglichst klein gehalten werden, also mehrmals Faltbar. Kann auf Vorder- und Rückseite bedruckt werden.
Ihrer Kreativität sind von unserer seite aus ,keine Grenzen gesetzt.
Im Anhang unser Logo , was mit auf den Flyer muss und in der Worddatei haben wir in Klammern noch Instruktionen für sie mit reingeschrieben. Design ect. ist Ihnen überlassen

```html
<!DOCTYPE html>
<html lang="de">
<head>
<meta charset="utf-8">
<title>Lunevia – Anleitung für ein ideales Raumklima</title>
<link href="https://fonts.googleapis.com/css2?family=Lato:wght@400;700&family=Cinzel:wght@400&display=swap" rel="stylesheet">
<style>
:root{
  --brand-blue:#0b7bc4;
  --box-blue:rgba(11,123,196,.9);
  --box-blue-soft:rgba(30,128,205,.82);
  --heading-blue:#1179c7;
  --panel-tint:#e6eef9;
  --table-stripe:#e3eefb;
  --table-head:#cfe2f7;
  --ink:#1b1b1b;
  --white:#ffffff;
  --navy:#2a2d7a;
}
*{margin:0;padding:0;box-sizing:border-box}
html,body{width:1200px;height:610px;overflow:hidden;background:var(--white)}
body{font-family:'Lato',sans-serif;color:var(--ink);position:relative}
.panel{position:absolute;overflow:hidden}
.photo{position:absolute;inset:0}
p{font-size:8.1px;line-height:10.2px}
h2{font-size:10px;font-weight:700;color:var(--heading-blue);line-height:11.5px}

/* top row */
.interior{left:0;top:0;width:300px;height:297px}
.interior .photo{background:linear-gradient(180deg,#e9ecef 0%,#dfe3e6 45%,#c9cdd1 70%,#e4e4e2 100%)}
.caption{position:absolute;left:0;top:214px;width:249px;height:70px;background:var(--box-blue);color:var(--white);padding:7px 10px 0 17px}
.caption p{line-height:10.3px}

.usage{left:300px;top:0;width:300px;height:297px;background:var(--panel-tint);padding:20px 19px 0 19px}
.usage h2{margin-bottom:9px}
.usage ol{list-style:none}
.usage li{font-size:8.1px;line-height:10.2px;margin-bottom:10px}

.airing{left:600px;top:0;width:300px;height:297px}
.airing .photo{background:linear-gradient(180deg,#3d7cc8 0%,#6fa1d9 40%,#b7d0ec 75%,#dfe9f5 100%)}
.airing-text{position:absolute;left:9px;top:12px;width:181px;height:269px;background:rgba(236,242,251,.93);padding:8px 7px 0 7px}
.airing-text h2{margin-bottom:9px}
.airing-text p{margin-bottom:10px}
.schedule{position:absolute;left:197px;top:94px;width:103px;height:159px;background:rgba(236,242,251,.95);padding:5px 6px}
.schedule h3{font-size:8.1px;font-weight:700;margin-bottom:10px}
.schedule dl{display:grid;grid-template-columns:54px auto;font-size:8.1px;line-height:10.2px}

.brand{left:900px;top:0;width:300px;height:297px;background:var(--white);text-align:center}
.brand-mark{position:absolute;left:126px;top:122px;width:48px;height:48px}
.brand-name{position:absolute;left:0;right:0;top:190px;font-family:'Lato',sans-serif;font-weight:400;font-size:19px;letter-spacing:4px;color:var(--ink)}
.brand-sub{position:absolute;left:0;right:0;top:226px;font-size:12.5px;font-weight:700}

/* bottom row */
.climate{left:0;top:297px;width:300px;height:300px;padding:38px 15px 0 15px}
.climate h2{margin-bottom:14px}
.climate h3{font-size:8.1px;font-weight:700;margin-bottom:10px}
.climate p{margin-bottom:9px}
.climate h4{font-size:8.3px;font-weight:700;color:var(--heading-blue);margin-bottom:9px}
.climate table{width:274px;border-collapse:collapse;font-size:8.1px}
.climate th{background:var(--table-head);text-align:left;font-weight:700;height:15.4px;padding:0 4px}
.climate td{height:15.3px;padding:0 4px}
.climate tr:nth-child(even) td{background:var(--table-stripe)}

.relax{left:300px;top:297px;width:600px;height:300px}
.relax .photo{background:radial-gradient(ellipse at 35% 30%,#a9c58a 0%,#cfdcc0 35%,#eef0ea 70%,#f6f7f5 100%)}
.note{position:absolute;background:var(--box-blue-soft);color:var(--white);padding:9px 13px 0 13px}
.note p{margin-bottom:10px}
.note-kitchen{left:42px;top:169px;width:258px;height:106px}
.note-facts{left:325px;top:109px;width:258px;height:163px}
.note-facts h3{font-size:8.3px;font-weight:700;margin-bottom:11px}

.review{left:900px;top:297px;width:300px;height:300px;background:var(--brand-blue);color:var(--white);text-align:center}
.stars{position:absolute;left:0;right:0;top:104px}
.review-text{position:absolute;left:0;right:0;top:144px;font-size:10.4px;font-weight:700;line-height:12.6px;text-transform:uppercase}
.review-text span{display:block;margin-bottom:13px}
</style>
</head>
<body>

<section class="panel interior">
  <div class="photo" role="img" aria-label="Helles Wohnzimmer mit Fenster, Heizkörper und Hängepflanze"></div>
  <div class="caption">
    <p>Die Verdunstungsdauer hängt von den verschiedensten Faktoren ab. Je gesättigter Ihre relative Luftfeuchtigkeit im Raum (durch schlechtes Lüften) und je kälter der Heizkörper desto Länger dauert der Verdunstungsprozess! Die Luft kann dadurch nicht mehr Feuchtigkeit aufnehmen!</p>
  </div>
</section>

<section class="panel usage">
  <h2>Was muss ich beachten und wie funktionieren meine neuen Lunevia Heizkörper Luftbefeuchter.</h2>
  <ol>
    <li>1. Füllen Sie Ihre neuen Luftbefeuchter mit warmen Wasser, idealerweise mit entkalktem Wasser.</li>
    <li>2. Sollten Sie kein entkalktes Wasser haben , sollten Sie Ihre Verdunster nach jedem Durchgang (Komplett Verdunstet) mit verdünntem Essig oder Zitronensäure von innen reinigen, um die Poren Kalkfrei zu halten und um eine optimale Verdunstung zu gewährleisten.</li>
    <li>3. Um weiterhin eine optimale Verdunstung zu gewährleisten, sollte Ihr Heizkörper so warm sein, dass Sie ihn gerade noch mit der Hand anfassen können oder noch heißer.</li>
    <li>4. Bringen Sie an jedem Heizkörper zwei Verdunster an. Außer im Bad und der Küche!</li>
    <li>5. Wenn die Verdunster zu lange an einem Heizkörper hängen, die abgeschaltet bzw. kalt sind ,dann kann es zur Tröpfchenbildung kommen, weil die Poren groß sind und bei kalter Oberfläche kann das Wasser nicht schnell genug verdunsten.</li>
  </ol>
</section>

<section class="panel airing">
  <div class="photo" role="img" aria-label="Blauer Himmel mit Wolken und fliegender Möwe"></div>
  <div class="airing-text">
    <h2>Richtiges Lüften</h2>
    <p>Schließen Sie den Thermostatkopf der Heizungen komplett. Öffnen Sie die Fenster zweier gegenüberliegender Räume gleichzeitig und lassen auch die Türen offen stehen.</p>
    <p>Auf diese Weise entsteht ein Durchzug und die warme, verbrauchte Luft zieht schneller nach draußen ab.</p>
    <p>Achtung: Vergessen Sie nicht, auch im zweiten Raum, den Heizkörper während des Lüftens abzustellen!</p>
    <p>Wie oft sollten Sie Lüften? Optimal wäre 4 mal am Tag, da dies aber oft nicht möglich ist, sollten Sie mindestens 2 mal am Tag Lüften, Abends vor dem Schlafen gehen und Morgens nach dem Aufstehen.</p>
    <p>Wenn Sie nun so vorgehen wie beschrieben, wird Ihnen und dem wunderbaren Gefühl eines schönen Klimas im Zuhause, nichts mehr im Wege stehen.</p>
  </div>
  <div class="schedule">
    <h3>Dauer des Lüftens:</h3>
    <dl>
      <dt>Januar</dt><dd>5 min</dd>
      <dt>Februar</dt><dd>5 min</dd>
      <dt>März</dt><dd>10 min</dd>
      <dt>April</dt><dd>15 min</dd>
      <dt>Mai</dt><dd>20 min</dd>
      <dt>Juni</dt><dd>30 min</dd>
      <dt>Juli</dt><dd>30 min</dd>
      <dt>August</dt><dd>30 min</dd>
      <dt>September</dt><dd>15 min</dd>
      <dt>Obtober</dt><dd>20 min</dd>
      <dt>November</dt><dd>10 min</dd>
      <dt>Dezember</dt><dd>5 min</dd>
    </dl>
  </div>
</section>

<section class="panel brand">
  <svg class="brand-mark" viewBox="0 0 48 48" aria-hidden="true"><circle cx="24" cy="24" r="22" fill="var(--navy)"/></svg>
  <div class="brand-name">LUNEVIA</div>
  <div class="brand-sub">Anleitung für ein ideales Raumklima</div>
</section>

<section class="panel climate">
  <h2>Für ein schönes Klima sorgen Sie, wie Folgt:</h2>
  <h3>relative Luftfeuchtigkeit in Wohnräumen</h3>
  <p>In der folgenden Tabelle finden Sie die optimalen Werte für relative Luftfeuchte und Temperatur in den verschiedenen Wohnbereichen. Als ideale Mittelwerte haben sich 40 - 60 % Feuchte und 20 °C Raumtemperatur bewährt.</p>
  <h4>Ideales Raumklima</h4>
  <table>
    <thead><tr><th>Raum</th><th>Optimale Temperatur</th><th>Optimale Luftfeuchtigkeit</th></tr></thead>
    <tbody>
      <tr><td>Wohnräume</td><td>20 °C</td><td>40 - 60 %</td></tr>
      <tr><td>Schlafzimmer</td><td>16 - 18 °C</td><td>40 - 60 %</td></tr>
      <tr><td>Kinderzimmer</td><td>20 - 22 °C</td><td>40 - 60 %</td></tr>
      <tr><td>Küche</td><td>18 °C</td><td>50 - 60 %</td></tr>
      <tr><td>Badezimmer</td><td>23 °C</td><td>50 - 70 %</td></tr>
      <tr><td>Keller</td><td>10 - 15 °C</td><td>50 - 65 %</td></tr>
    </tbody>
  </table>
</section>

<section class="panel relax">
  <div class="photo" role="img" aria-label="Entspannte Person ruht im hellen Raum vor grünem Hintergrund"></div>
  <div class="note note-kitchen">
    <p>Naturgemäß liegt die Luftfeuchte in Küche und Bad etwas höher und kann beim Kochen oder Duschen auch über diese Werte steigen.</p>
    <p>Das ist kein Problem, solange der Zustand nicht dauerhaft anhält. Dennoch sollte es Ihnen zur Gewohnheit werden, sofort nach dem Kochen oder Duschen den Wasserdampf nach draußen entweichen zu lassen.</p>
  </div>
  <div class="note note-facts">
    <h3>Wissenswertes zur Luftfeuchtigkeit</h3>
    <p>Das gesündeste Raumklima herrscht bei 50 % relativer Luftfeuchte und 20 °C Raumtemperatur.</p>
    <p>Die relative Raumfeuchte sollte nicht unter 30 % fallen.</p>
    <p>Einige Schimmelpilzarten vermehren sich bereits ab 70 % Feuchtigkeit.</p>
    <p>Herrschen über einen längeren Zeitraum mehr als 80 % Feuchtigkeit im Raum, führt das unvermeidlich zur Entstehung von Schimmel.</p>
  </div>
</section>

<section class="panel review">
  <svg class="stars" width="300" height="14" viewBox="0 0 300 14" aria-label="Fünf Sterne">
    <g fill="var(--white)">
      <polygon transform="translate(110,0)" points="6,0 7.8,4.6 12,4.8 8.7,7.6 9.8,12 6,9.5 2.2,12 3.3,7.6 0,4.8 4.2,4.6"/>
      <polygon transform="translate(125,0)" points="6,0 7.8,4.6 12,4.8 8.7,7.6 9.8,12 6,9.5 2.2,12 3.3,7.6 0,4.8 4.2,4.6"/>
      <polygon transform="translate(140,0)" points="6,0 7.8,4.6 12,4.8 8.7,7.6 9.8,12 6,9.5 2.2,12 3.3,7.6 0,4.8 4.2,4.6"/>
      <polygon transform="translate(155,0)" points="6,0 7.8,4.6 12,4.8 8.7,7.6 9.8,12 6,9.5 2.2,12 3.3,7.6 0,4.8 4.2,4.6"/>
      <polygon transform="translate(170,0)" points="6,0 7.8,4.6 12,4.8 8.7,7.6 9.8,12 6,9.5 2.2,12 3.3,7.6 0,4.8 4.2,4.6"/>
    </g>
  </svg>
  <div class="review-text">
    <span>Sie sind zufrieden mit unserem Produkt<br>und dieser Anleitung?</span>
    <span>Dann hinterlassen Sie uns doch bitte<br>eine Rezension auf Volkarn.</span>
  </div>
</section>

</body>
</html>
```